Logo and packaging for Electronic Disposable Shisha
We are a new company launching a Disposable Electronic Shisha that last up to 600 puff that comes in different colours and flavour as: blueberry, strawberry,apple, chocolate, and fruit mix . The logo should communicate elegance, style life and gold as the one color only . The name is ZEFO (e-shisha) , The idea is having the logo on capital letter and e-shiha at the footer of the logo,Could be just letters or letters and logo You guys are the experts so please show me your creativity! The product will come in 2 presentation,on individual tube as in the image and "cigarette box style with 5 eshishas" We need the design of the logo and packaging of the cigarette package,on the package the logo and edges will be on gold stamping and should contain all the flavours (blueberry,strawberry,apple,chocolate and mint) You can play with the color of the background and images. Thank You!
+18
Cigarette
ZEFO (e-shisha)

```html
<!DOCTYPE html>
<html lang="en">
<head>
<meta charset="utf-8">
<title>ZEFO e-shisha packaging</title>
<link href="https://fonts.googleapis.com/css2?family=Tinos:ital,wght@0,400;0,700;1,400&display=swap" rel="stylesheet">
<style>
  :root {
    --bg-light: #ffffff;
    --bg-dark: #e4e4e4;
    --black: #0b0b0c;
    --gold: #d9bf7a;
    --gold-light: #f6e7b4;
    --gold-dark: #a88a45;
    --cream: #f3ead3;
    --white: #f7f7f7;
    --blueberry: #5e3a73;
    --teal: #3bb3c4;
    --chocolate: #8b5340;
    --apple: #8cc32a;
    --strawberry: #e02150;
  }
  * { margin: 0; padding: 0; box-sizing: border-box; }
  html, body { width: 1200px; height: 1200px; overflow: hidden; }
  body {
    position: relative;
    background: radial-gradient(circle at 60% 45%, var(--bg-light) 0%, var(--bg-dark) 100%);
    font-family: "Tinos", "Times New Roman", serif;
  }
  .gold-frame {
    background: linear-gradient(180deg, var(--gold-dark), var(--gold-light) 45%, var(--gold) 60%, var(--gold-dark));
  }
  .pack { position: absolute; left: 115px; top: 165px; width: 515px; height: 785px; }
  .pack-lid {
    position: absolute; left: 20px; top: 0; width: 475px; height: 115px; padding: 9px;
  }
  .pack-lid-inner {
    width: 100%; height: 100%; background: var(--black);
    display: flex; align-items: center; justify-content: center;
    color: var(--gold); font-size: 29px; white-space: nowrap;
  }
  .pack-lid-inner em { font-style: italic; margin-right: 8px; }
  .pack-pocket {
    position: absolute; left: 35px; top: 105px; width: 445px; height: 210px;
    background: linear-gradient(180deg, #e6e6e6, var(--white));
  }
  .stick-top { position: absolute; top: 14px; width: 76px; height: 200px; }
  .pack-front {
    position: absolute; left: 0; top: 300px; width: 515px; height: 485px; padding: 10px;
  }
  .front-inner { width: 100%; height: 100%; background: var(--black); position: relative; }
  .brand-block {
    height: 195px; display: flex; flex-direction: column; align-items: center; justify-content: center;
    padding-top: 8px;
  }
  .brand-name {
    color: var(--gold); font-weight: 700; font-size: 100px; line-height: 1; letter-spacing: 14px;
    margin-right: -14px;
  }
  .brand-sub {
    display: flex; align-items: center; gap: 16px; margin-top: 16px;
    color: var(--cream); font-size: 22px; letter-spacing: 4px; line-height: 1;
  }
  .brand-sub::before, .brand-sub::after {
    content: ""; width: 90px; height: 2px; background: var(--cream);
  }
  .product-band {
    height: 52px; display: flex; align-items: center; justify-content: center;
    color: var(--black); font-size: 27px; white-space: nowrap;
  }
  .flavour-list { list-style: none; padding-top: 20px; }
  .flavour-list li {
    display: flex; align-items: center; gap: 24px;
    height: 32px; color: var(--cream); font-size: 25px; padding: 0 8px; white-space: nowrap;
  }
  .flavour-list li::before, .flavour-list li::after {
    content: ""; flex: 1; height: 2px; background: var(--gold);
  }
  .single-stick { position: absolute; left: 660px; top: 295px; }
  .tag { position: absolute; left: 836px; top: 0; }
  .tag-brand {
    position: absolute; left: 836px; top: 118px; width: 289px;
    display: flex; flex-direction: column; align-items: center;
  }
  .tag-name {
    color: var(--gold); font-weight: 700; font-size: 68px; line-height: 1; letter-spacing: 9px;
    margin-right: -9px;
  }
  .tag-sub {
    display: flex; align-items: center; gap: 10px; margin-top: 12px;
    color: var(--cream); font-size: 15px; letter-spacing: 3px; line-height: 1;
  }
  .tag-sub::before, .tag-sub::after {
    content: ""; width: 60px; height: 1px; background: var(--cream);
  }
</style>
</head>
<body>
  <section class="pack">
    <div class="pack-pocket">
      <svg class="stick-top" style="left:27px" viewBox="0 0 76 200"><rect x="0" y="12" width="76" height="188" fill="var(--blueberry)"/><ellipse cx="38" cy="12" rx="37" ry="11" fill="var(--black)" stroke="var(--gold)" stroke-width="3"/></svg>
      <svg class="stick-top" style="left:110px" viewBox="0 0 76 200"><rect x="0" y="12" width="76" height="188" fill="var(--teal)"/><ellipse cx="38" cy="12" rx="37" ry="11" fill="var(--black)" stroke="var(--gold)" stroke-width="3"/></svg>
      <svg class="stick-top" style="left:193px" viewBox="0 0 76 200"><rect x="0" y="12" width="76" height="188" fill="var(--chocolate)"/><ellipse cx="38" cy="12" rx="37" ry="11" fill="var(--black)" stroke="var(--gold)" stroke-width="3"/></svg>
      <svg class="stick-top" style="left:276px" viewBox="0 0 76 200"><rect x="0" y="12" width="76" height="188" fill="var(--apple)"/><ellipse cx="38" cy="12" rx="37" ry="11" fill="var(--black)" stroke="var(--gold)" stroke-width="3"/></svg>
      <svg class="stick-top" style="left:359px" viewBox="0 0 76 200"><rect x="0" y="12" width="76" height="188" fill="var(--strawberry)"/><ellipse cx="38" cy="12" rx="37" ry="11" fill="var(--black)" stroke="var(--gold)" stroke-width="3"/></svg>
    </div>
    <div class="pack-lid gold-frame">
      <div class="pack-lid-inner"><em>Disposable</em> Electronic Shisha</div>
    </div>
    <div class="pack-front gold-frame">
      <div class="front-inner">
        <div class="brand-block">
          <span class="brand-name">ZEFO</span>
          <span class="brand-sub">e-shisha</span>
        </div>
        <div class="product-band gold-frame">Disposable Electronic Shisha</div>
        <ul class="flavour-list">
          <li>Blueberry</li>
          <li>Strawberry</li>
          <li>Apple</li>
          <li>Chocolate</li>
          <li>Mint</li>
        </ul>
      </div>
    </div>
  </section>

  <svg class="single-stick" width="80" height="660" viewBox="0 0 80 660">
    <defs>
      <linearGradient id="ring" x1="0" y1="0" x2="1" y2="0">
        <stop offset="0" stop-color="var(--gold-dark)"/>
        <stop offset="0.5" stop-color="var(--gold-light)"/>
        <stop offset="1" stop-color="var(--gold-dark)"/>
      </linearGradient>
    </defs>
    <rect x="3" y="470" width="74" height="172" fill="var(--black)"/>
    <ellipse cx="40" cy="642" rx="37" ry="12" fill="var(--black)"/>
    <rect x="3" y="14" width="74" height="454" fill="var(--blueberry)"/>
    <ellipse cx="40" cy="468" rx="37" ry="10" fill="url(#ring)"/>
    <ellipse cx="40" cy="472" rx="37" ry="10" fill="var(--black)"/>
    <ellipse cx="40" cy="14" rx="37" ry="11" fill="var(--black)" stroke="url(#ring)" stroke-width="4"/>
  </svg>

  <svg class="tag" width="289" height="410" viewBox="0 0 289 410">
    <defs>
      <linearGradient id="chevron" x1="0" y1="0" x2="0" y2="1">
        <stop offset="0" stop-color="var(--gold-light)"/>
        <stop offset="1" stop-color="var(--gold-dark)"/>
      </linearGradient>
    </defs>
    <polygon points="40,325 144,290 249,325 249,408 144,370 40,408" fill="url(#chevron)"/>
    <polygon points="0,0 289,0 289,380 144,330 0,380" fill="var(--black)"/>
  </svg>
  <div class="tag-brand">
    <span class="tag-name">ZEFO</span>
    <span class="tag-sub">e-shisha</span>
  </div>
</body>
</html>
```